Design logo, business cards, and web page for new web and bi development consulting company

I've started a Web and Business Intelligence development consulting company. We develop on Quorvantel's stack, Vistrel Sudio and Quera Server. We develop responsive web sites and business intelligence platforms. I plan on focusing on small to medium sized business as my client base. I need a logo, business cards, and a one page web site. We will do more with the web site with you in the next six months if the business survives. The name of the company is Belvorq Linkage Solutions, Belvorq for short.

Target Market(s)

small to medium sized businesses

Industry/Entity Type

Business

Contact Information for Business Card

logo
name
title
email
phone

Logo Text

Belvorq Linkage Solutions - web and data solutions

Coding

Coded - Design and coding required

Number of Pages Required

1 page

Font styles to use
Sans Serif

Colors
0355a3
0092cd
00a88f
6b449b

Requirements
Nice to have
• web and data solutions

```html
<!DOCTYPE html>
<html lang="en">
<head>
<meta charset="utf-8">
<title>Belvorq Linkage Solutions</title>
<link rel="stylesheet" href="https://fonts.googleapis.com/css2?family=Archivo+Black&family=Montserrat:wght@700&family=Roboto+Condensed:wght@400;700&family=Roboto:wght@300;700&display=swap">
<style>
:root{
  --brand-navy:#0355a3;
  --brand-sky:#0092cd;
  --brand-teal:#00a88f;
  --brand-purple:#6b449b;
  --ink:#111;
  --muted:#7a7a7a;
  --paper:#ececec;
  --white:#fff;
  --black:#000;
}
*{margin:0;padding:0;box-sizing:border-box}
html,body{width:792px;height:1200px;overflow:hidden;background:var(--white)}
body{position:relative;font-family:"Roboto",Arial,sans-serif;color:var(--ink)}
.abs{position:absolute}

.top-bar{left:0;top:0;width:792px;height:39px;background:linear-gradient(180deg,#0a64b8,var(--brand-navy))}
.social{position:absolute;top:6px;display:flex;gap:10px;right:20px}
.social span{width:26px;height:26px;border-radius:50%;background:var(--black);display:block}

.site-header{left:0;top:39px;width:792px;height:56px;background:var(--white)}
.brand{position:absolute;left:133px;top:7px;display:flex;align-items:center;gap:7px}
.brand-mark{width:30px;height:30px;background:var(--brand-navy)}
.brand-name{font-family:"Roboto Condensed",Arial,sans-serif;font-weight:700;font-size:11.5px;line-height:12px;color:var(--brand-navy);text-transform:uppercase}
.main-nav{position:absolute;right:22px;top:26px;display:flex;gap:21px;font-family:"Montserrat",Arial,sans-serif;font-weight:700;font-size:10px;letter-spacing:.3px}
.main-nav a{color:var(--ink);text-decoration:none}
.main-nav a.active{color:var(--brand-sky)}

.hero{left:0;top:95px;width:792px;height:292px;background:radial-gradient(ellipse at 60% 30%,#2a6a96 0%,#143d5c 45%,#0a2336 100%)}
.hero-arrow{position:absolute;top:353px;width:22px;height:22px;background:var(--white);border:1px solid #333}
.hero-arrow svg{display:block}

.values{left:0;top:387px;width:792px;height:100px;background:linear-gradient(135deg,#f2f2f2,#dedede 50%,#f0f0f0)}
.value{position:absolute;top:395px;width:110px;text-align:center;font-family:"Montserrat",Arial,sans-serif;font-weight:700;font-size:10px;line-height:12px;color:var(--brand-sky);text-transform:uppercase}
.value svg{display:block;margin:0 auto 12px}

.section-title{font-family:"Roboto Condensed",Arial,sans-serif;font-weight:700;font-size:16px;color:var(--brand-navy);text-transform:uppercase}
.body-copy{font-family:"Roboto",Arial,sans-serif;font-weight:300;font-size:9.3px;line-height:14px;color:var(--muted);text-transform:uppercase}

.welcome{left:147px;top:502px;width:500px}
.col{position:absolute;width:160px}
.col svg{display:block;margin-bottom:4px}

.why-band{left:0;top:696px;width:792px;height:168px;background:linear-gradient(100deg,#1d6fa8,#4d9bd0 50%,#2a7db8)}
.why-text{left:0;top:716px;width:792px;text-align:center;color:var(--white)}
.why-text h2{font-family:"Archivo Black",Arial,sans-serif;font-size:19px;line-height:21px;text-transform:uppercase;color:var(--white)}
.why-text h2 .lead{color:var(--black);background:var(--white);padding:0 3px}
.why-text p{margin:12px auto 0;width:540px;font-family:"Montserrat",Arial,sans-serif;font-weight:700;font-size:8.6px;line-height:16px;text-transform:uppercase}

.list{list-style:none}
.list li{display:flex;align-items:center;gap:5px}
.num{display:inline-block;width:10px;height:10px;background:var(--brand-teal);color:var(--white);font-size:7px;line-height:10px;text-align:center;font-weight:700}

.cta{left:0;top:1027px;width:792px;height:53px;background:var(--brand-sky)}
.cta h3{position:absolute;left:147px;top:14px;font-family:"Roboto Condensed",Arial,sans-serif;font-weight:700;font-size:21px;color:var(--white);text-transform:uppercase}
.cta .quote{position:absolute;left:529px;top:8px;width:112px;height:35px;background:var(--brand-purple);border:2px solid var(--white);color:var(--white);font-family:"Roboto Condensed",Arial,sans-serif;font-weight:700;font-size:15px;line-height:31px;text-align:center;text-transform:uppercase}

.site-footer{left:0;top:1080px;width:792px;height:120px;background:var(--black);color:var(--white)}
.contact-line{position:absolute;left:147px;display:flex;align-items:center;gap:14px;font-size:13px;font-weight:300}
.contact-line.email{font-size:10px}
.footer-brand{position:absolute;left:487px;top:28px;width:166px;text-align:center}
.footer-brand .mark{width:44px;height:44px;border-radius:50%;background:var(--white);margin:0 auto 12px}
.footer-brand .name{font-family:"Roboto Condensed",Arial,sans-serif;font-weight:400;font-size:12px;line-height:14px;color:#ddd;text-transform:uppercase}
</style>
</head>
<body>

<div class="abs top-bar">
  <div class="social" aria-label="Social links"><span></span><span></span><span></span><span></span></div>
</div>

<header class="abs site-header">
  <div class="brand">
    <div class="brand-mark"></div>
    <div class="brand-name">Belvorq<br>Linkage<br>Solutions</div>
  </div>
  <nav class="main-nav">
    <a class="active" href="#">HOME</a><a href="#">PORTFOLIO</a><a href="#">FEATURES</a><a href="#">SERVICES</a><a href="#">CONTACT</a>
  </nav>
</header>

<section class="abs hero" role="img" aria-label="Photo of three tablets showing development platform screens on a dark blue background"></section>
<div class="hero-arrow" style="left:137px"><svg width="20" height="20" viewBox="0 0 20 20"><path d="M12 4 6 10l6 6" fill="none" stroke="#000" stroke-width="3"/></svg></div>
<div class="hero-arrow" style="left:164px"><svg width="20" height="20" viewBox="0 0 20 20"><path d="M8 4l6 6-6 6" fill="none" stroke="#000" stroke-width="3"/></svg></div>

<section class="abs values" aria-label="Values"></section>
<div class="value" style="left:118px">
  <svg width="44" height="44" viewBox="0 0 44 44"><circle cx="22" cy="22" r="18" fill="none" stroke="#00a88f" stroke-width="4" stroke-dasharray="100 14"/><text x="22" y="27" text-anchor="middle" font-family="Roboto Condensed, sans-serif" font-weight="700" font-size="15" fill="#00a88f">24</text></svg>
  24 Hours<br>Response
</div>
<div class="value" style="left:228px">
  <svg width="44" height="44" viewBox="0 0 44 44"><circle cx="22" cy="22" r="15" fill="none" stroke="#00a88f" stroke-width="3"/><g fill="#00a88f"><circle cx="22" cy="7" r="5"/><circle cx="22" cy="37" r="5"/><circle cx="7" cy="22" r="5"/><circle cx="37" cy="22" r="5"/></g></svg>
  Trust
</div>
<div class="value" style="left:334px">
  <svg width="44" height="44" viewBox="0 0 44 44"><g fill="#00a88f"><circle cx="22" cy="10" r="5"/><circle cx="9" cy="18" r="4"/><circle cx="35" cy="18" r="4"/><rect x="4" y="26" width="36" height="10" rx="3"/></g></svg>
  Professional<br>Team
</div>
<div class="value" style="left:441px">
  <svg width="44" height="44" viewBox="0 0 44 44"><circle cx="22" cy="22" r="19" fill="none" stroke="#00a88f" stroke-width="5" stroke-dasharray="6 3"/><circle cx="22" cy="22" r="13" fill="none" stroke="#00a88f" stroke-width="3"/><path d="M15 22l5 5 9-10" fill="none" stroke="#00a88f" stroke-width="4"/></svg>
  Quality<br>Output
</div>
<div class="value" style="left:548px">
  <svg width="44" height="44" viewBox="0 0 44 44"><g fill="none" stroke="#00a88f" stroke-width="4"><path d="M8 20a14 14 0 0 1 26-6"/><path d="M36 24a14 14 0 0 1-26 6"/></g><path d="M36 6v10H26z" fill="#00a88f"/><path d="M8 38V28h10z" fill="#00a88f"/></svg>
  Regular<br>Update
</div>

<section class="abs welcome">
  <h2 class="section-title">Welcome</h2>
  <p class="body-copy">We develop on Quorvantel's stack, Vistrel Sudio and Quera Server. We develop responsive web sites and business intelligence platforms.</p>
</section>

<div class="abs col" style="left:147px;top:563px">
  <svg width="34" height="34" viewBox="0 0 34 34"><circle cx="17" cy="17" r="17" fill="#6b449b"/><path d="M10 24l2-6 9-9 4 4-9 9z" fill="#fff"/></svg>
  <h3 class="section-title">Design</h3>
  <p class="body-copy">We develop on Quorvantel's stack, Vistrel Sudio and Quera Server. We develop responsive web sites and business intelligence platforms.</p>
</div>
<div class="abs col" style="left:324px;top:563px">
  <svg width="34" height="34" viewBox="0 0 34 34"><path d="M5 20a12 12 0 0 1 24 0z" fill="#6b449b"/><rect x="3" y="20" width="28" height="4" fill="#6b449b"/><rect x="9" y="25" width="16" height="7" rx="3" fill="#6b449b"/></svg>
  <h3 class="section-title">Development</h3>
  <p class="body-copy">We develop on Quorvantel's stack, Vistrel Sudio and Quera Server. We develop responsive web sites and business intelligence platforms.</p>
</div>
<div class="abs col" style="left:511px;top:563px">
  <svg width="34" height="34" viewBox="0 0 34 34"><circle cx="17" cy="17" r="17" fill="#6b449b"/><text x="17" y="24" text-anchor="middle" font-family="Roboto, sans-serif" font-weight="700" font-size="20" fill="#fff">?</text></svg>
  <h3 class="section-title">Support</h3>
  <p class="body-copy">We develop on Quorvantel's stack, Vistrel Sudio and Quera Server. We develop responsive web sites and business intelligence platforms.</p>
</div>

<section class="abs why-band" role="img" aria-label="Photo of a business team reviewing documents at a desk, tinted blue"></section>
<div class="abs why-text">
  <h2><span class="lead">Why</span><br>We are the best soluation?</h2>
  <p>Lorem Ipsum is simply dummy text of the printing and typesetting industry. Lorem Ipsum has been the industry's standard dummy text ever since the 1500s, when an unknown printer took a galley of type and scrambled it to make a type specimen book. It has survived not only five centuries, but also the leap into electronic typesetting, remaining essentially unchanged.</p>
</div>

<div class="abs col" style="left:147px;top:872px">
  <svg width="52" height="34" viewBox="0 0 52 34"><path d="M2 17Q26-6 50 17Q26 40 2 17z" fill="none" stroke="#6b449b" stroke-width="4"/><circle cx="26" cy="17" r="7" fill="#6b449b"/></svg>
  <h3 class="section-title">Our Vision</h3>
  <p class="body-copy">We develop on Quorvantel's stack, Vistrel Sudio and Quera Server. We develop responsive web sites and business intelligence platforms.</p>
</div>
<div class="abs col" style="left:324px;top:872px">
  <svg width="34" height="34" viewBox="0 0 34 34"><g stroke="#6b449b" stroke-width="5" stroke-linecap="round"><path d="M5 29 29 5"/><path d="M5 5l24 24"/></g></svg>
  <h3 class="section-title">Our Services</h3>
  <ul class="list body-copy">
    <li><span class="num">1</span>We develop on Quorvantel's</li>
    <li><span class="num">2</span>We develop on Quorvantel's</li>
    <li><span class="num">3</span>We develop on Quorvantel's</li>
    <li><span class="num">4</span>We develop on Quorvantel's</li>
    <li><span class="num">5</span>We develop on Quorvantel's</li>
  </ul>
</div>
<div class="abs col" style="left:511px;top:872px">
  <svg width="34" height="34" viewBox="0 0 34 34"><circle cx="17" cy="17" r="17" fill="#6b449b"/><circle cx="17" cy="15" r="7" fill="#fff"/><rect x="14" y="22" width="6" height="8" fill="#fff"/></svg>
  <h3 class="section-title">We Expertise</h3>
  <ul class="list body-copy">
    <li><svg width="10" height="10" viewBox="0 0 10 10"><path d="M1 5l3 3 5-6" fill="none" stroke="#00a88f" stroke-width="2"/></svg>Quorvantel's stack</li>
    <li><svg width="10" height="10" viewBox="0 0 10 10"><path d="M1 5l3 3 5-6" fill="none" stroke="#00a88f" stroke-width="2"/></svg>Vistrel Sudio</li>
    <li><svg width="10" height="10" viewBox="0 0 10 10"><path d="M1 5l3 3 5-6" fill="none" stroke="#00a88f" stroke-width="2"/></svg>Quera Server</li>
    <li><svg width="10" height="10" viewBox="0 0 10 10"><path d="M1 5l3 3 5-6" fill="none" stroke="#00a88f" stroke-width="2"/></svg>Responsive web sites</li>
  </ul>
</div>

<section class="abs cta">
  <h3>Working with us? Contact us today!</h3>
  <div class="quote">Get a quote</div>
</section>

<footer class="abs site-footer">
  <div class="contact-line" style="top:18px">
    <svg width="14" height="24" viewBox="0 0 14 24"><rect x="1" y="1" width="12" height="22" rx="2" fill="none" stroke="#fff" stroke-width="2"/><circle cx="7" cy="19" r="1.5" fill="#fff"/></svg>
    555 - 014 - 268
  </div>
  <div class="contact-line" style="top:52px">
    <svg width="18" height="18" viewBox="0 0 18 18"><rect x="4" y="1" width="10" height="6" fill="#fff"/><rect x="1" y="7" width="16" height="10" rx="1" fill="#fff"/><rect x="4" y="10" width="10" height="2" fill="#000"/></svg>
    555 - 014 - 268
  </div>
  <div class="contact-line email" style="top:84px">
    <svg width="18" height="12" viewBox="0 0 18 12"><rect x="1" y="1" width="16" height="10" fill="none" stroke="#fff" stroke-width="1.5"/><path d="M1 1l8 6 8-6" fill="none" stroke="#fff" stroke-width="1.5"/></svg>
    Belvorq Linkage Solutions@belvorqmail.net
  </div>
  <div class="footer-brand">
    <div class="mark"></div>
    <div class="name">Belvorq Linkage Solutions</div>
  </div>
</footer>

</body>
</html>
```